Finch Essential Oils - Body Oils

I am in need of 4 different label and package designs for a new line of body oils that I am launching. I already have the logo and names, it is now a matter of positioning the content. The names are as follows;

1) CARDAMOM + CYPRESS
WARMING BODY OIL
2) NEROLI + LEMON
UPLIFTING BODY OIL
3) CEDAR + BIRCH
GROUNDING BODY OIL
4) SAGE + MINT
COOLING BODY OIL.
The size of each label is 13cm wide x 9.5cm high. The size of the box is 4.5cm x 4.5cm x 15.5cm high.
The size of the bottle is 4cm across the base and 10.5cm in glass height.
I have included an image from a line that I started to work on but it didn't go anywhere. I thought the borders looked good to frame it in however, I am not attached to anything at this point. I am also including a picture of a product line that has used different colors on the packaging. I am not certain that this is the direction I'd like to take however I like how it looks with them. If we were to add the color I think it should be JUST the boxes and NOT the labels and they would be as follows; WARMING OIL - warm burgundy, earth tones UPLIFTING OIL - warm light, lightish blues GROUNDING OIL - warm soft, brownish creams COOLING OIL - refreshing light, pale green possibly blue. I would be interested to see what adding a sprig of a plant would look like on the boxes however with the already busy logo it might look like too much is going on. As you will see in our instagram and website we currently have the bear logo in a foil. I am not sure that I want to proceed with this foil as it is difficult to photograph. I would like to look at colors that compliment the existing line of essential oils as well as the dark brown wood on the cap.
I have added a design that looks a bit industrial that I like, it reads black ops.

Target Market(s)

My market is mainly females who are interested in natural health age 17 - 70. There is a large movement for organic + green beauty. I would like the label to look and feel clean and natural. Something that has been wildcrafted, raw and completely from nature.

Industry/Entity Type

Health And Wellness

Colors

Designer to choose colors to be used in the design.

Requirements
Must have
• Appeal to very progressive organic consumers. Please see the pictures marked SAMPLES 1, 2, 3 + 4 for design ideas.
• Easy to read. Clean design.
• The following information should be on the label as well as the packaging box.
• Size - 100 ML
• Barcodes - still to come
• Ingredients:
• 1) CARDAMOM + CYPRESS WARMING BODY OIL - *Sunflower Oil, **Orange, **Cardamom, **Cypress, **Ginger *Organic, **Organic essential oil
• 2) NEROLI + LEMON UPLIFTING BODY OIL - *Sunflower oil, **Orange, **Neroli, **Grapefruit, **Lemon, **Bergamot, **Benzoin, *Organic, **Organic essential oil
• 3) CEDAR + BIRCH GROUNDING BODY OIL - *Sunflower Oil, **Cedarwood, **Birch, **Benzoin, **Patchouli,*Organic, **Organic essential oil
• 4) SAGE + MINT COOLING BODY OIL - *Sunflower oil, **Spearmint, **Clary Sage, **Geranium, **Ylang Ylang, *Organic, **Organic essential oil
• Suggested Use:
• Warm oil if desired. Apply to the full body after bathing, massage in motions toward the heart until the oil is mostly absorbed. Can also be added to bath water.
Nice to have
• I would like to see the designs on the actual bottle (pic included) to see how it looks.
Should not have
• Bright colors.

```html
<!DOCTYPE html>
<html lang="en">
<head>
<meta charset="utf-8">
<title>Finch Essential Oils – Cardamom | Cypress Warming Body Oil</title>
<link href="https://fonts.googleapis.com/css2?family=Barlow+Condensed:wght@500;600&display=swap" rel="stylesheet">
<style>
  :root {
    --page: #ffffff;
    --paper: #f7f6f4;
    --ink: #4a4542;
    --rule: #5a5552;
    --burgundy: #861420;
    --burgundy-deep: #6e0f19;
    --gold: #c8a06a;
    --gold-soft: #e6d3b5;
    --cream: #f1e4cf;
  }
  * { box-sizing: border-box; margin: 0; padding: 0; }
  html, body { width: 1200px; height: 1200px; overflow: hidden; background: var(--page); }
  body {
    position: relative;
    font-family: "Barlow Condensed", "Arial Narrow", sans-serif;
    color: var(--ink);
  }

  .panel {
    position: absolute;
    background: var(--paper);
    overflow: hidden;
    box-shadow: 0 0 0 1px #e4e1dd;
  }

  .label { left: 70px; top: 230px; width: 400px; height: 740px; }
  .box-front { left: 540px; top: 160px; width: 320px; height: 900px; }
  .box-side { left: 860px; top: 160px; width: 270px; height: 900px; background: #efedea; }

  .brand-block {
    position: absolute;
    left: 0; right: 0;
    display: flex;
    flex-direction: column;
    align-items: center;
  }
  .label .brand-block { top: 70px; }
  .box-front .brand-block { top: 250px; }

  .brand-mark {
    width: 86px; height: 86px;
    border-radius: 50%;
    background: var(--gold);
    margin-bottom: 22px;
  }
  .brand-name {
    font-size: 40px;
    font-weight: 500;
    letter-spacing: 0.2px;
    color: var(--ink);
    line-height: 1;
  }
  .rule {
    width: 76%;
    height: 2px;
    background: var(--rule);
    margin: 14px 0;
  }
  .scent {
    font-size: 30px;
    font-weight: 600;
    letter-spacing: 0.5px;
    line-height: 1;
  }
  .type {
    font-size: 29px;
    font-weight: 500;
    text-align: center;
    line-height: 1.1;
    letter-spacing: 0.6px;
  }

  .band {
    position: absolute;
    left: 0; right: 0; bottom: 0;
    background: linear-gradient(180deg, var(--burgundy) 0%, var(--burgundy-deep) 100%);
  }
  .label .band { height: 240px; }
  .box-front .band, .box-side .band { height: 240px; }

  .sprigs {
    position: absolute;
    left: 0; right: 0;
  }
  .label .sprigs { bottom: 150px; height: 140px; }
  .box-front .sprigs, .box-side .sprigs { bottom: 140px; height: 200px; }
  .sprigs {
    background: linear-gradient(180deg, rgba(200,160,106,0) 0%, rgba(200,160,106,0.28) 45%, rgba(134,20,32,0.55) 80%, rgba(134,20,32,0) 100%);
  }

  .size {
    position: absolute;
    left: 0; right: 0;
    text-align: center;
    font-size: 28px;
    font-weight: 500;
    color: var(--cream);
  }
  .label .size { bottom: 50px; }
  .box-front .size, .box-side .size { bottom: 56px; }

  .usage {
    position: absolute;
    top: 330px;
    left: 40px; right: 40px;
    padding: 16px 0;
    border-top: 2px solid var(--rule);
    border-bottom: 2px solid var(--rule);
    text-align: center;
    font-size: 19px;
    font-weight: 500;
    line-height: 1.3;
  }
  .usage-title { font-weight: 600; margin-bottom: 4px; }
</style>
</head>
<body>

  <section class="panel label" aria-label="Bottle label">
    <div class="brand-block">
      <div class="brand-mark"></div>
      <p class="brand-name">Finch Essential Oils</p>
      <div class="rule"></div>
      <p class="scent">CARDAMOM | CYPRESS</p>
      <div class="rule"></div>
      <p class="type">WARMING<br>BODY OIL</p>
      <div class="rule"></div>
    </div>
    <div class="band"></div>
    <div class="sprigs" role="img" aria-label="Gold line drawing of cardamom pods and cypress sprigs"></div>
    <p class="size">100 ml</p>
  </section>

  <section class="panel box-front" aria-label="Box front panel">
    <div class="brand-block">
      <div class="brand-mark"></div>
      <p class="brand-name">Finch Essential Oils</p>
      <div class="rule"></div>
      <p class="scent">CARDAMOM | CYPRESS</p>
      <div class="rule"></div>
      <p class="type">WARMING<br>BODY OIL</p>
      <div class="rule"></div>
    </div>
    <div class="band"></div>
    <div class="sprigs" role="img" aria-label="Gold line drawing of cardamom pods and cypress sprigs"></div>
    <p class="size">100 ml</p>
  </section>

  <section class="panel box-side" aria-label="Box side panel">
    <div class="usage">
      <p class="usage-title">Suggested Use:</p>
      <p>Warm oil if desired. Apply to the full body after bathing, massage in motions toward the heart until the oil is mostly absorbed. Can also be added to bath water.</p>
    </div>
    <div class="band"></div>
    <div class="sprigs" role="img" aria-label="Gold line drawing of cardamom pods and cypress sprigs"></div>
  </section>

</body>
</html>
```